Vantorix Business
Card and Letter Head
Creative Brief
Professional
Dalton Prewitt
Owner
7153 Hollow Creek Christiansted, Kessler Bay VX 00941
sales@vantorix.net
vantorix.net
Custom Integrator
ultimate digital experience

```html
<!DOCTYPE html>
<html lang="en">
<head>
<meta charset="utf-8">
<title>Vantorix Business Cards</title>
<link href="https://fonts.googleapis.com/css2?family=Roboto:wght@400;700&display=swap" rel="stylesheet">
<style>
  :root {
    --canvas: #ffffff;
    --charcoal: #2b2b2b;
    --charcoal-deep: #1c1c1c;
    --charcoal-light: #3d3d3d;
    --cream: #f4f0d6;
    --cream-deep: #d9d1a4;
    --gold-text: #6d6230;
    --ink: #3a3a2a;
    --white: #ffffff;
  }
  * { margin: 0; padding: 0; box-sizing: border-box; }
  html, body { width: 1200px; height: 221px; overflow: hidden; background: var(--canvas); }
  body { font-family: "Roboto", Arial, sans-serif; position: relative; }

  .card {
    position: absolute; top: 6px; width: 392px; height: 209px; overflow: hidden;
  }
  .card--front-plain { left: 0; }
  .card--front-pattern { left: 404px; }
  .card--back { left: 808px; }

  .brand-panel {
    position: absolute; left: 0; top: 0; width: 140px; height: 100%;
    background: linear-gradient(160deg, var(--charcoal-light), var(--charcoal-deep));
    box-shadow: 3px 0 6px rgba(0,0,0,.35);
  }
  .brand-panel--pattern {
    background: radial-gradient(circle at 40% 40%, #4a4a4a, var(--charcoal-deep) 75%);
  }
  .brand-mark {
    position: absolute; left: 28px; top: 60px; width: 44px; height: 44px;
    border-radius: 50%; border: 2px solid #8a8a8a; background: #3a3a3a;
  }
  .brand-name {
    position: absolute; left: 10px; top: 150px;
    color: var(--white); font-weight: 700; font-size: 18px; letter-spacing: 1px;
  }

  .info-panel {
    position: absolute; left: 140px; top: 0; right: 0; height: 100%;
    background: linear-gradient(135deg, var(--cream) 0%, #ebe4bb 55%, var(--cream-deep) 100%);
  }
  .person { position: absolute; right: 28px; top: 10px; text-align: center; color: var(--gold-text); }
  .person__name { font-weight: 700; font-size: 13px; letter-spacing: .5px; text-transform: uppercase; }
  .person__title { font-size: 10px; text-transform: uppercase; letter-spacing: .5px; }

  .contact {
    position: absolute; right: 24px; top: 100px; width: 170px;
    text-align: center; color: var(--ink); font-size: 6.5px; line-height: 10px;
    text-transform: uppercase; letter-spacing: .2px;
  }

  .back-field {
    position: absolute; inset: 0;
    background: radial-gradient(ellipse at 50% 45%, #4a4a4a 0%, var(--charcoal) 45%, var(--charcoal-deep) 100%);
  }
  .back-lockup {
    position: absolute; left: 0; right: 0; top: 58px; text-align: center;
  }
  .back-lockup .brand-mark {
    position: static; display: block; margin: 0 auto 14px; width: 46px; height: 46px;
    border-color: var(--white); background: #2f2f2f;
  }
  .back-lockup .brand-name {
    position: static; font-size: 28px; letter-spacing: 1.5px;
  }
</style>
</head>
<body>

<section class="card card--front-plain">
  <div class="brand-panel">
    <span class="brand-mark"></span>
    <span class="brand-name">VANTORIX</span>
  </div>
  <div class="info-panel">
    <div class="person">
      <p class="person__name">Dalton Prewitt</p>
      <p class="person__title">Owner</p>
    </div>
    <div class="contact">
      <p>7153 Hollow Creek Christiansted</p>
      <p>Kessler Bay VX 00941</p>
      <p>Ph: 340 555 0142 &nbsp;Fax: 340 555 0187</p>
      <p>Email: sales@vantorix.net</p>
      <p>vantorix.net</p>
    </div>
  </div>
</section>

<section class="card card--front-pattern">
  <div class="brand-panel brand-panel--pattern" role="img" aria-label="Dark panel with a faint large lion head decoration">
    <span class="brand-mark"></span>
    <span class="brand-name">VANTORIX</span>
  </div>
  <div class="info-panel">
    <div class="person">
      <p class="person__name">Dalton Prewitt</p>
      <p class="person__title">Owner</p>
    </div>
    <div class="contact">
      <p>7153 Hollow Creek Christiansted</p>
      <p>Kessler Bay VX 00941</p>
      <p>Ph: 340 555 0142 &nbsp;Fax: 340 555 0187</p>
      <p>Email: sales@vantorix.net</p>
      <p>vantorix.net</p>
    </div>
  </div>
</section>

<section class="card card--back">
  <div class="back-field" role="img" aria-label="Charcoal background with a faint large lion head decoration"></div>
  <div class="back-lockup">
    <span class="brand-mark"></span>
    <span class="brand-name">VANTORIX</span>
  </div>
</section>

</body>
</html>
```